Label Design for a sexy ladies 5 pocket skinny

We need modern packaging design for women's skinny 5 pocket pants for a brand name Tarnel. All kinds of packaging designs are welcome.
The pant is folded and packaged in a poly bag. We require a label design for the brand name Tarnel. The main label will be attached by a string on the belt loop. the size of that label will 25cm in length and 10cm wide. This is the first label the customer see's when she picks up the garment. Therefore, we require an eye catching design for that. If required it could have certain information about the pant on the main label such as Comfort fit, Wrinkle-resistant, machine washable, luxury fabric. But, if you feel that adding the above information spoils the design of the label then it is not a must to include the above information. On the back of the label we like to include the information that this pant was manufactured in an Oskel Platinum certified green plant and hence the damage to the environment because of the plant is nill.
The second label is attached on to the waist band and the purpose of that label is to include the size of the pant such 32x32. The size of that label is 8cm in length and 4cm in width. There is no design on the back on this label it has to be blank.
Sample is given for what we currently use for our mens chino pant. we are looking for something very different.
Reason: because there was a delay in the project being approved by pixel harbor.
Environment

```html
<!DOCTYPE html>
<html lang="en">
<head>
<meta charset="utf-8">
<title>Tarnel — Skinny 5 Pocket Pant Labels</title>
<link rel="stylesheet" href="https://fonts.googleapis.com/css2?family=Cinzel:wght@500;600&family=Dancing+Script:wght@700&family=Arimo:wght@700&display=swap">
<style>
  :root {
    --backdrop: #c68a52;
    --ink: #2d1417;
    --ink-soft: #3a2320;
    --paper-light: #dcc0ac;
    --paper-mid: #c8a691;
    --paper-dark: #b08c78;
    --white: #f4f1ee;
    --badge: #9b9b9b;
    --badge-light: #cfcfcf;
    --silhouette: #4a3c34;
  }
  * { margin: 0; padding: 0; box-sizing: border-box; }
  html, body { width: 1200px; height: 900px; overflow: hidden; }
  body { background: var(--backdrop); position: relative; font-family: "Cinzel", serif; }

  .label { position: absolute; overflow: hidden; }
  .paper { background: linear-gradient(160deg, var(--paper-light) 0%, var(--paper-mid) 55%, var(--paper-dark) 100%); }
  .label svg.edges { position: absolute; inset: 0; width: 100%; height: 100%; }

  /* Front hang tag */
  .hang-front { left: 125px; top: 92px; width: 283px; height: 705px; }
  .brand-name {
    position: absolute; left: 42px; top: 128px; z-index: 2;
    font-family: "Arimo", sans-serif; font-weight: 700; font-size: 66px;
    color: var(--ink); letter-spacing: -1px;
  }
  .model-figure {
    position: absolute; left: 14px; top: 222px; width: 128px; height: 400px; z-index: 1;
    background: linear-gradient(180deg, rgba(58,35,32,.55), rgba(58,35,32,.2));
    border-radius: 36px 36px 10px 10px;
  }
  .features { position: absolute; left: 133px; top: 384px; list-style: none; z-index: 2; }
  .features li {
    font-size: 13px; font-weight: 500; color: var(--ink); line-height: 26.5px;
    font-variant: small-caps;
  }
  .features li::before { content: "•"; margin-right: 6px; }
  .product-line {
    position: absolute; right: 10px; top: 502px; text-align: right; z-index: 2;
    font-family: "Dancing Script", cursive; font-size: 27px; line-height: 30px;
    color: var(--ink-soft);
  }

  /* Back hang tag */
  .hang-back { left: 499px; top: 90px; width: 283px; height: 707px; background: var(--ink); }
  .eco-statement {
    position: absolute; top: 38px; left: 0; width: 100%; text-align: center;
    color: var(--white); font-size: 15px; font-weight: 600; line-height: 22.4px;
    letter-spacing: .5px;
  }
  .cert-badge {
    position: absolute; left: 61px; top: 313px; width: 160px; height: 160px; z-index: 2;
    border-radius: 50%; background: var(--badge); border: 8px solid var(--badge-light);
  }
  .deer-mark {
    position: absolute; left: 128px; top: 432px; width: 155px; height: 275px; z-index: 1;
    background: linear-gradient(180deg, rgba(74,60,52,.35), rgba(74,60,52,.8));
    border-radius: 60px 30px 0 0;
  }
  .brush-patch {
    position: absolute; left: 0; top: 585px; width: 190px; height: 122px; z-index: 2;
    background: radial-gradient(ellipse at 40% 60%, var(--white) 55%, rgba(244,241,238,0) 75%);
  }
  .tagline {
    position: absolute; left: 8px; top: 634px; z-index: 3;
    font-family: "Dancing Script", cursive; font-size: 19px; line-height: 24px;
    color: var(--ink);
  }

  /* Waistband size label */
  .size-label { left: 907px; top: 355px; width: 112px; height: 225px; }
  .size-text {
    position: absolute; left: 0; top: 37px; width: 100px; text-align: center;
    font-size: 17px; font-weight: 500; line-height: 27px; color: var(--ink);
  }
</style>
</head>
<body>

<section class="label hang-front paper" aria-label="Tarnel front hang tag">
  <svg class="edges" viewBox="0 0 283 705" preserveAspectRatio="none" aria-hidden="true">
    <polygon fill="var(--ink)" points="0,0 283,0 283,36 275,44 267,36 259,44 251,36 243,44 235,36 227,44 219,36 211,44 203,36 195,44 187,36 179,44 171,36 163,44 155,36 147,44 139,36 131,44 123,36 115,44 107,36 99,44 91,36 83,44 75,36 67,44 59,36 51,44 43,36 35,44 27,36 19,44 11,36 0,44"/>
    <polygon fill="var(--ink)" points="0,705 283,705 283,652 275,660 267,652 259,660 251,652 243,660 235,652 227,660 219,652 211,660 203,652 195,660 187,652 179,660 171,652 163,660 155,652 147,660 139,652 131,660 123,652 115,660 107,652 99,660 91,652 83,660 75,652 67,660 59,652 51,660 43,652 35,660 27,652 19,660 11,652 0,660"/>
  </svg>
  <div class="brand-name">Tarnel</div>
  <div class="model-figure" role="img" aria-label="Sketch of a woman in skinny jeans seen from behind"></div>
  <ul class="features">
    <li>Comfort fit</li>
    <li>Wrinkle-resistant</li>
    <li>machine washable</li>
    <li>luxury fabric</li>
  </ul>
  <p class="product-line">women's skinny<br>5 pocket pants</p>
</section>

<section class="label hang-back" aria-label="Tarnel back hang tag">
  <p class="eco-statement">THIS TARNEL 5<br>POKET PANT<br>WAS PROUDLY<br>PRODUCED IN<br>AN OSKEL<br>PLATINUM<br>CERTIFIED<br>GREEN PLANT<br>WITH NO<br>NEGATIVE<br>ENVIROMETAL<br>IMPACT</p>
  <div class="cert-badge" role="img" aria-label="Green building certification badge"></div>
  <div class="deer-mark" role="img" aria-label="Faint deer silhouette decoration"></div>
  <div class="brush-patch" role="img" aria-label="White brush stroke texture"></div>
  <p class="tagline">help the environment,<br>buy a tarnel</p>
</section>

<section class="label size-label paper" aria-label="Waistband size label">
  <svg class="edges" viewBox="0 0 112 225" preserveAspectRatio="none" aria-hidden="true">
    <polygon fill="var(--ink)" points="112,60 112,225 100,225 106,215 99,205 105,195 98,185 104,175 97,165 103,155 97,145 103,135 98,125 104,115 99,105 105,95 100,85 106,75 104,65"/>
    <polygon fill="var(--ink)" points="0,0 22,0 12,8 18,16 8,24 12,30 0,36"/>
  </svg>
  <p class="size-text">32<br>WAIST<br>x<br>32<br>LENGTH</p>
</section>

</body>
</html>
```